New website for selling opensource software business to business

Website K7 Software

The open source software industry has grown enormously in recent years. More and more customers from software companies choose an open source solution. K7 Software is going to fulfill this increasing demand.

Core business

Reselling software subcriptions (business to business).

Side business

Selling consultancy and Training to customers

Goals:

- Binding of customers to K7 IT Group
- Sales of subscriptions to customer
- Enlarge network K7 IT Group
- USP: Sales of complete package, Software, consultancy and training

Products

There are a couple of products/ services that K7 will provide. Below you will find an overview of the Products:

- Bluefox subscriptions
- Crater subscriptions
- Velmor products
- Customized consultancy for the customer
- Customized training for the customer

Style

Behind the website should be a cms system like pagecraft.

Target Market(s)

Business - Business

Industry/Entity Type

Business

Coding

Coded - Design and coding required

Number of Pages Required

5+ page

Font styles to use
Other font styles liked:
• Calibri

Colors
0355a3
3176b5
85abd2

Requirements
Must have
• Home page with large photo background, About us, contact page with safe option to request more info
• Portfolio pages:
• 4 pages with a product group each:
• 1. Blue fox
• 2. Craters
• 3. Velmor
• 4. Ourtrustwall
• 1. Blue Fox
• On top space for short info/bullets about Blue fox. Further, a grid with 8 columns. In the columns 2 buttons both lead to a popup. A popup for information and a popup for requesting a quote.
• 2. Crater:
• On top space for short info/bullets about Crater. Further, a grid with 3 columns. In the columns 2 buttons both lead to a popup. A popup for information and a popup for requesting a quote.
• 1. Velmor:
• On top space for short info/bullets about Velmor. Further, a grid with 4 columns. In the columns 2 buttons both lead to a popup. A popup for information and a popup for requesting a quote.
• 2. Ourtrustwall:
• On top space for short info/bullets about Ourtrustwall. Further, a grid with 2 columns. In the columns 2 buttons both lead to a popup. A popup for information and a popup for requesting a quote.

```html
<!DOCTYPE html>
<html lang="en">
<head>
<meta charset="utf-8">
<title>K7 Software</title>
<link href="https://fonts.googleapis.com/css2?family=Lato:wght@400;700;900&display=swap" rel="stylesheet">
<style>
:root{
  --blue-dark:#0355a3;
  --blue-mid:#3176b5;
  --blue-light:#85abd2;
  --ink:#222;
  --body:#444;
  --card-line:#d6d6d6;
  --grey-band:#efefef;
  --white:#fff;
}
*{margin:0;padding:0;box-sizing:border-box}
html,body{width:1200px;height:2748px;overflow:hidden}
body{position:relative;font-family:'Lato',sans-serif;color:var(--ink);background:var(--white)}
.abs{position:absolute}
.btn{position:absolute;display:flex;align-items:center;justify-content:center;border-radius:22px;
  background:linear-gradient(#2f72c0,var(--blue-dark));color:var(--white);font-size:13px;font-weight:700;letter-spacing:.3px;text-transform:uppercase}
.center{text-align:center}

/* hero */
.hero{left:0;top:0;width:1200px;height:586px;background:linear-gradient(160deg,#8d9096 0%,#5d6168 45%,#3f4349 100%)}
.hero-shade{left:0;top:0;width:1200px;height:586px;background:rgba(20,25,35,.25)}
.brand{left:77px;top:33px;display:flex;align-items:center;gap:14px}
.brand-dot{width:91px;height:91px;border-radius:50%;background:var(--white)}
.brand-name{position:absolute;left:0;top:0;width:91px;height:91px;display:flex;align-items:center;justify-content:center;font-size:17px;font-weight:900;color:var(--blue-dark);text-align:center;line-height:1.1}
.nav a{position:absolute;top:66px;color:var(--white);font-size:13px;font-weight:700;text-decoration:none}
.nav .active{left:467px;top:59px;width:97px;height:38px;border-radius:19px;background:var(--blue-mid);display:flex;align-items:center;justify-content:center}
.demo{left:916px;top:53px;width:211px;height:48px;border:2px solid var(--white);border-radius:24px;background:#1b1e22;color:var(--white);font-size:20px;font-weight:700;display:flex;align-items:center;justify-content:center}
.hero-title{left:0;width:1200px;top:210px;font-size:74px;font-weight:700;color:var(--white)}
.hero-sub{left:0;width:1200px;top:292px;font-size:29px;font-weight:700;color:var(--white)}
.slider-dots{display:flex;gap:8px}
.slider-dots span{width:10px;height:10px;border-radius:50%;background:var(--white)}
.slider-dots .off{background:transparent;border:1.5px solid var(--white)}

/* portfolio */
.section-title{left:0;width:1200px;font-size:27px;font-weight:400;color:var(--ink);text-transform:uppercase}
.card{top:696px;width:242px;height:295px;border:1.5px solid var(--card-line);background:var(--white)}
.card-mark{position:absolute;left:0;top:40px;width:100%;display:flex;align-items:center;justify-content:center;gap:10px;font-size:30px;font-weight:700;color:var(--ink)}
.card-mark i{width:30px;height:30px;border-radius:50%;background:var(--blue-dark)}
.card-name{position:absolute;left:0;top:110px;width:100%;font-size:20px;font-weight:700;color:var(--blue-dark);text-transform:uppercase}
.card-text{position:absolute;left:18px;right:18px;top:140px;font-size:13.5px;line-height:22px;color:var(--body)}

/* about */
.about{left:0;top:1041px;width:1200px;height:370px;background:radial-gradient(ellipse at 50% 60%,#85abd2 0%,#5f93c8 35%,#3176b5 75%)}
.about-title{left:0;width:1200px;top:1094px;font-size:27px;font-weight:700;color:var(--white)}
.about-text{left:160px;width:880px;top:1141px;font-size:15px;line-height:28px;color:var(--white)}
.pillar{top:1228px;width:200px}
.pillar .disc{width:84px;height:84px;border-radius:50%;background:var(--white);margin:0 auto;display:flex;align-items:center;justify-content:center}
.pillar p{margin-top:18px;font-size:17px;font-weight:700;color:var(--white);text-transform:uppercase}

/* features */
.photo{background:linear-gradient(135deg,#c9ccd1,#8d939b)}
.feature-title{font-size:27px;font-weight:700;line-height:33px;color:var(--ink);text-transform:uppercase}
.feature-text{font-size:14.5px;line-height:24.5px;color:var(--body)}

/* blog */
.blog{left:0;top:2215px;width:1200px;height:372px;background:var(--grey-band)}
.post-title{font-size:17px;font-weight:700;color:var(--blue-dark);text-transform:uppercase}
.post-text{font-size:14px;line-height:24px;color:var(--body)}
.post-more{font-size:12px;font-weight:700;color:var(--blue-dark);text-transform:uppercase}

/* footer */
.footer{left:0;top:2587px;width:1200px;height:161px;background:var(--blue-dark)}
.foot-nav span{position:absolute;top:2628px;font-size:12.5px;font-weight:700;color:var(--white)}
.copy{left:75px;top:2667px;font-size:11.5px;line-height:20px;color:var(--white)}
.follow{left:945px;top:2628px;font-size:12.5px;font-weight:700;color:var(--white)}
.social{top:2670px;width:20px;height:20px;border-radius:50%;background:var(--white)}
</style>
</head>
<body>

<!-- hero -->
<div class="abs hero" role="img" aria-label="Business team in suits gathered around a laptop in an office"></div>
<div class="abs hero-shade"></div>
<div class="abs brand"><div class="brand-dot"></div><div class="brand-name">K7<br>Software</div></div>
<nav class="nav">
  <a class="active">HOME</a>
  <a style="left:583px">ABOUT US</a>
  <a style="left:694px">PORTFOLIO</a>
  <a style="left:815px">CONTACT US</a>
</nav>
<div class="abs demo">REQUEST DEMO</div>
<h1 class="abs hero-title center">K7 Software</h1>
<p class="abs hero-sub center">We are selling open source software for B2B companies.</p>
<div class="btn" style="left:509px;top:348px;width:156px;height:42px">Read More</div>
<div class="abs slider-dots" style="left:571px;top:546px"><span class="off"></span><span></span><span></span><span></span></div>

<!-- portfolio -->
<h2 class="abs section-title center" style="top:634px">Portfolio</h2>

<div class="abs card" style="left:75px">
  <div class="card-mark"><i></i>bluefox</div>
  <div class="card-name center">Bluefox</div>
  <p class="card-text center">Vestibulum ante ipsum primis in faucibus orci luctus et ultrices posuere cubilia</p>
  <div class="btn" style="left:41px;top:224px;width:158px;height:42px">Click Here</div>
</div>
<div class="abs card" style="left:344px">
  <div class="card-mark"><i></i>crater</div>
  <div class="card-name center">Crater</div>
  <p class="card-text center">Vestibulum ante ipsum primis in faucibus orci luctus et ultrices posuere cubilia</p>
  <div class="btn" style="left:41px;top:224px;width:158px;height:42px">Click Here</div>
</div>
<div class="abs card" style="left:614px">
  <div class="card-mark"><i></i>Velmor</div>
  <div class="card-name center">Velmor</div>
  <p class="card-text center">Vestibulum ante ipsum primis in faucibus orci luctus et ultrices posuere cubilia</p>
  <div class="btn" style="left:41px;top:224px;width:158px;height:42px">Click Here</div>
</div>
<div class="abs card" style="left:883px">
  <div class="card-mark" style="font-size:17px"><i></i>OURTRUSTWALL</div>
  <div class="card-name center">Ourtrustwall</div>
  <p class="card-text center">Vestibulum ante ipsum primis in faucibus orci luctus et ultrices posuere cubilia</p>
  <div class="btn" style="left:41px;top:224px;width:158px;height:42px">Click Here</div>
</div>

<!-- about -->
<div class="abs about"></div>
<h2 class="abs about-title center">ABOUT K7 SOFTWARE</h2>
<p class="abs about-text center">The open source software industry has grown enormously in recent years. More and more customers from software companies choose an open source solution. K7 Software is going to fulfill this increasing demand.</p>

<div class="abs pillar center" style="left:230px">
  <div class="disc"><svg width="36" height="30" viewBox="0 0 36 30"><rect x="12" y="1" width="12" height="7" rx="2" fill="none" stroke="#0355a3" stroke-width="3"/><rect x="1" y="7" width="34" height="22" rx="3" fill="#0355a3"/></svg></div>
  <p>Core Business</p>
</div>
<div class="abs pillar center" style="left:499px">
  <div class="disc"><svg width="40" height="40" viewBox="0 0 40 40"><rect x="17" y="4" width="21" height="16" fill="none" stroke="#0355a3" stroke-width="2.5"/><circle cx="9" cy="10" r="4" fill="#0355a3"/><rect x="5" y="15" width="8" height="14" fill="#0355a3"/><rect x="5" y="28" width="3" height="10" fill="#0355a3"/><rect x="10" y="28" width="3" height="10" fill="#0355a3"/><line x1="12" y1="17" x2="20" y2="13" stroke="#0355a3" stroke-width="2.5"/></svg></div>
  <p>Side Business</p>
</div>
<div class="abs pillar center" style="left:770px">
  <div class="disc"><svg width="38" height="38" viewBox="0 0 38 38"><circle cx="18" cy="20" r="15" fill="none" stroke="#0355a3" stroke-width="3"/><circle cx="18" cy="20" r="8" fill="none" stroke="#0355a3" stroke-width="3"/><circle cx="18" cy="20" r="2.5" fill="#0355a3"/><line x1="18" y1="20" x2="34" y2="4" stroke="#0355a3" stroke-width="3"/></svg></div>
  <p>Our Goals</p>
</div>

<!-- features -->
<div class="abs photo" style="left:75px;top:1455px;width:524px;height:359px" role="img" aria-label="Business people in a meeting at a table with a laptop"></div>
<h3 class="abs feature-title" style="left:634px;top:1484px">Customized Consultancy<br>for the Customer</h3>
<p class="abs feature-text" style="left:634px;top:1559px;width:492px">Aliquam molestie, mi et imperdiet euismod, dui purus auctor tellus, et interdum lacus lectus et ante. Sed accumsan sollicitudin sapien, sit amet adipiscing turpis gravida ac. In congue, neque ac lobortis volutpat, libero mauris varius mi, vitae suscipit ipsum ligula vitae risus. Duis aliquam nibh a dui iaculis viverra id a velit.</p>
<div class="btn" style="left:636px;top:1722px;width:155px;height:40px">Click Here</div>

<h3 class="abs feature-title" style="left:75px;top:1854px">Customized Training for<br>the Customer</h3>
<p class="abs feature-text" style="left:75px;top:1929px;width:494px">Aliquam molestie, mi et imperdiet euismod, dui purus auctor tellus, et interdum lacus lectus et ante. Sed accumsan sollicitudin sapien, sit amet adipiscing turpis gravida ac. In congue, neque ac lobortis volutpat, libero mauris varius mi, vitae suscipit ipsum ligula vitae risus. Duis aliquam nibh a dui iaculis viverra id a velit.</p>
<div class="btn" style="left:75px;top:2092px;width:158px;height:40px">Click Here</div>
<div class="abs photo" style="left:601px;top:1814px;width:524px;height:359px;background:linear-gradient(135deg,#e6e9ee,#aab8c9)" role="img" aria-label="Colleagues looking together at a computer screen"></div>

<!-- blog -->
<div class="abs blog"></div>
<h2 class="abs section-title center" style="top:2261px">Recent Blog Posts</h2>

<div class="abs photo" style="left:75px;top:2321px;width:214px;height:150px;background:linear-gradient(135deg,#3a5f95,#142848)" role="img" aria-label="Presenter in front of a software slide"></div>
<h4 class="abs post-title" style="left:317px;top:2318px">Aliquam Molestie Mi</h4>
<p class="abs post-text" style="left:317px;top:2346px;width:250px">Sed accumsan sollicitudin sapien, sit amet adipiscing turpis gravida ac. In congue, neque ac lobortis volutpat, libero mauris varius mi..</p>
<span class="abs post-more" style="left:317px;top:2456px">Read More</span>

<div class="abs photo" style="left:614px;top:2321px;width:214px;height:150px;background:linear-gradient(135deg,#5d6e7e,#2b3440)" role="img" aria-label="Hands typing on a laptop keyboard"></div>
<h4 class="abs post-title" style="left:856px;top:2318px">Aliquam Molestie Mi</h4>
<p class="abs post-text" style="left:856px;top:2346px;width:250px">Sed accumsan sollicitudin sapien, sit amet adipiscing turpis gravida ac. In congue, neque ac lobortis volutpat, libero mauris varius mi..</p>
<span class="abs post-more" style="left:856px;top:2456px">Read More</span>

<div class="abs slider-dots" style="left:578px;top:2521px"><span style="background:#3176b5"></span><span style="background:#666"></span><span style="background:#666"></span></div>

<!-- footer -->
<div class="abs footer"></div>
<div class="foot-nav">
  <span style="left:75px">HOME</span>
  <span style="left:152px">ABOUT US</span>
  <span style="left:255px">PORTFOLIO</span>
  <span style="left:367px">CONTACT US</span>
</div>
<p class="abs copy">Copyright © 2017. Company Name.<br>All Right Reserved</p>
<span class="abs follow">FOLLOW US</span>
<span class="abs social" style="left:941px"></span>
<span class="abs social" style="left:981px"></span>
<span class="abs social" style="left:1021px"></span>
<span class="abs social" style="left:1062px"></span>
<span class="abs social" style="left:1102px"></span>

</body>
</html>
```